Small Ecommerce Styled Site to Sell / Lease Domain Names

We have a small portfolio of 100+ domain names that we would like to offer for sale or lease via a web site. Along the lines of http://www.velmorhosts.example/searchdomain.html?priceChoice=2&sort=leasing_desc

We would like initially a 4 page design, listing page (as site referenced above), domain info page (Universal Domain Name Landing Page with form) and checkout a page and About Us Page

We do not want a replica of the site listed, please use it as a guide only, we are looking for a fresh design, in similar concept web 2.0

Our Colours are #351a41 (Main) - #ffca27 (Secondary) all other colours must compliment those 2.
Updates

Domain Landing Page:  I am sorry I was not clear about expectations, however we would like a domain landing page that would be the default holding page for a domain name.

For some examples of what I mean please see:
https://www.qarsibex.example.au/guest-articles/7626-domain-for-sale-landing-pages.html
http://dev.plinthwardexchange.example/blog/2013/09/sales-only-landers-and-buy-it-now-2/

Industry/Entity Type

Domain

Font styles to use
Sans Serif

```html
<!DOCTYPE html>
<html lang="en">
<head>
<meta charset="utf-8">
<title>Quellmark Leasing – Find a domain on lease</title>
<link rel="stylesheet" href="https://fonts.googleapis.com/css2?family=Noticia+Text&family=Open+Sans:wght@400;600&display=swap">
<style>
:root{
  --plum:#351a41;
  --plum-deep:#2a1434;
  --plum-soft:#5a3a6b;
  --gold:#ffca27;
  --gold-pale:#ffeeb8;
  --ink:#3a2a40;
  --grey:#8a8a8a;
  --line:#e2e2e2;
  --white:#ffffff;
}
*{box-sizing:border-box;margin:0;padding:0}
html,body{width:820px;height:1200px;overflow:hidden;background:var(--white)}
body{position:relative;font-family:"Open Sans",sans-serif;color:var(--ink)}
.abs{position:absolute}
.serif{font-family:"Noticia Text",serif}

/* header */
.site-header{left:0;top:0;width:820px;height:40px;background:var(--white)}
.brand{left:122px;top:8px;display:flex;align-items:center;gap:6px;font-family:"Noticia Text",serif;font-size:18px;color:var(--plum)}
.brand-dot{width:20px;height:20px;border-radius:50%;background:var(--plum-soft)}
.main-nav{left:318px;top:12px;display:flex;gap:18px;font-family:"Noticia Text",serif;font-size:13px;color:var(--plum)}
.main-nav .current{border-bottom:1px solid var(--gold);padding-bottom:3px}
.social-bar{left:585px;top:0;display:flex}
.social-bar span{width:29px;height:40px;background:var(--gold);border-left:1px solid #f0b800}
.social-bar span:first-child{background:var(--plum)}

/* hero */
.hero{left:0;top:40px;width:820px;height:328px;background:var(--plum)}
.hero-art{left:60px;top:0;width:700px;height:328px;background:radial-gradient(ellipse 55% 70% at 45% 20%,#d9c8e0 0%,#a58bb3 35%,#5a3a6b 70%,var(--plum) 100%)}
.hero-title{left:0;top:140px;width:820px;text-align:center;font-size:36px;color:var(--plum);padding-left:10px}
.hero-sub{left:0;top:186px;width:820px;text-align:center;font-size:14px;letter-spacing:4px;color:var(--plum)}
.btn-video{left:326px;top:221px;width:163px;height:32px;background:var(--gold);display:flex;align-items:center;justify-content:center;gap:8px;font-family:"Noticia Text",serif;font-size:14px;color:var(--plum)}
.btn-video i{width:24px;height:15px;background:var(--plum);border-radius:2px;position:relative}
.btn-video i::after{content:"";position:absolute;left:9px;top:3px;border-left:7px solid var(--white);border-top:4.5px solid transparent;border-bottom:4.5px solid transparent}
.search-panel{left:231px;top:331px;width:348px;height:37px;background:rgba(53,26,65,.85)}
.field{top:338px;height:22px;background:var(--white);font-size:9px;color:#9a9a9a;padding:5px 10px}
.field-domain{left:238px;width:143px}
.field-cat{left:387px;width:142px}
.btn-search{left:535px;top:338px;width:37px;height:22px;background:var(--gold)}

/* categories */
.category-band{left:0;top:368px;width:820px;height:32px;background:var(--gold);display:flex;align-items:center;justify-content:center;gap:10px;font-size:9.5px;color:var(--plum)}
.category-band span{display:flex;align-items:center;gap:5px;white-space:nowrap}
.category-band svg{width:13px;height:11px;fill:var(--plum)}

/* intro */
.intro{left:0;top:400px;width:820px;height:181px;background:var(--plum)}
.notch{left:360px;top:400px;width:100px;height:34px}
.more{left:400px;top:404px;width:21px;height:21px;border:1.5px solid var(--gold);border-radius:50%;color:var(--gold);font-size:16px;line-height:17px;text-align:center}
.intro-text{left:175px;top:457px;width:470px;text-align:center;font-size:11px;line-height:18.5px;color:var(--white)}
.intro-text .lead{color:var(--gold)}

/* portfolio */
.portfolio{left:0;top:581px;width:820px;height:301px;background:var(--gold)}
.section-title{display:flex;align-items:center;gap:16px;font-family:"Noticia Text",serif;font-size:25px;color:var(--plum);white-space:nowrap}
.portfolio-title{left:219px;top:610px}
.table-card{left:116px;top:669px;width:578px;height:213px;background:var(--white)}
.tab{top:687px;height:24px;font-size:10.5px;letter-spacing:1px;color:#777;text-align:center;line-height:24px;background:#ececec}
.tab.active{background:var(--gold-pale);color:#8a7a50}
.meta{left:155px;top:724px;font-size:8.5px;color:#555;display:flex;align-items:center;gap:6px}
.meta b{font-weight:600}
.pager{left:362px;top:724px;display:flex;gap:13px;font-size:9px;color:#777}
.pager .on{color:var(--plum);font-weight:600}
.sort{left:568px;top:722px;width:89px;height:17px;border:1px solid var(--line);font-size:8px;color:#888;padding:3px 8px}
.col-head{top:752px;font-size:8px;font-weight:600;letter-spacing:.5px;color:var(--plum)}
.row{left:152px;width:504px;height:16px;font-size:8.5px}
.row .name{position:absolute;left:0;top:2px;color:#888}
.row .cat{position:absolute;left:133px;top:2px;color:#777;font-size:7px;display:flex;gap:4px;align-items:center}
.row .cat i{width:7px;height:7px;border:1px solid #888;border-radius:50%}
.row .fee{position:absolute;left:323px;top:0;width:63px;height:15px;background:var(--gold);border:1px solid #d9a800;font-size:8px;font-weight:600;color:var(--plum);text-align:center;line-height:13px}
.row .offer{position:absolute;left:439px;top:0;width:64px;height:15px;border:1px solid var(--plum);font-size:8px;font-weight:600;color:var(--plum);text-align:center;line-height:13px;letter-spacing:.5px}
.scroll{left:667px;top:686px;width:12px;height:196px}
.scroll-track{left:667px;top:702px;width:12px;height:162px;background:#f1f1f1}
.scroll-thumb{left:667px;top:722px;width:12px;height:76px;background:var(--plum)}

/* featured */
.featured-title{left:222px;top:912px}
.carousel{left:112px;top:972px;width:600px;height:42px}
.feature-row{left:142px;top:975px;width:530px;display:flex;justify-content:space-between}
.feature{display:flex;align-items:center;gap:5px;font-size:12.5px;color:var(--ink);white-space:nowrap}
.feature i{flex:none;width:36px;height:36px;border-radius:50%;background:var(--plum);border:3px solid #6b4d7a}

/* footer */
.site-footer{left:0;top:1036px;width:820px;height:156px;background:var(--plum);color:var(--white)}
.foot-col h3{font-family:"Noticia Text",serif;font-weight:400;font-size:17px;margin-bottom:10px}
.foot-col ul{list-style:none;font-size:9.5px;line-height:18.7px}
.follow li{display:flex;align-items:center;gap:7px;margin-bottom:4.3px}
.follow li i{width:17px;height:17px;border-radius:50%;background:var(--white)}
.news-input{left:544px;top:1082px;width:158px;height:20px;background:var(--white);font-size:8px;color:#aaa;padding:5px 12px}
.btn-subscribe{left:544px;top:1106px;width:158px;height:21px;background:var(--gold);font-size:8.5px;font-weight:600;color:var(--plum);text-align:center;line-height:21px}
.free-note{left:550px;top:1139px;font-size:9px}
.btn-signup{left:637px;top:1136px;width:65px;height:21px;border:1px solid var(--white);font-size:11px;text-align:center;line-height:19px}
</style>
</head>
<body>

<header class="site-header abs">
  <div class="brand abs"><span class="brand-dot"></span>Quellmark Leasing</div>
  <nav class="main-nav abs"><span class="current">Home</span><span>Domain</span><span>Information</span><span>About</span></nav>
  <div class="social-bar abs" aria-label="Social links"><span></span><span></span><span></span><span></span></div>
</header>

<section class="hero abs">
  <div class="hero-art abs" role="img" aria-label="Tilted domain listing sheet with a magnifying glass, glowing on the plum background"></div>
</section>
<h1 class="hero-title abs serif" style="font-weight:400">find a domain on Lease</h1>
<p class="hero-sub abs serif">WITH JUST FEW CLICKS!</p>
<div class="btn-video abs">WATCH A VIDEO <i></i></div>
<div class="search-panel abs"></div>
<div class="field field-domain abs">Enter Your Domain</div>
<div class="field field-cat abs">Choose The Categories</div>
<div class="btn-search abs"><svg width="37" height="22" viewBox="0 0 37 22"><circle cx="17" cy="10" r="6" fill="none" stroke="#351a41" stroke-width="1.8"/><line x1="21.5" y1="14.5" x2="25" y2="18" stroke="#351a41" stroke-width="2"/></svg></div>

<nav class="category-band abs">
  <span><svg viewBox="0 0 13 11"><rect x="2" y="1" width="9" height="6"/><rect x="0" y="8" width="13" height="2"/></svg>Computers and Internet</span>
  <span><svg viewBox="0 0 13 11"><rect x="1" y="4" width="11" height="4" rx="1"/><circle cx="3.5" cy="9" r="1.6"/><circle cx="9.5" cy="9" r="1.6"/></svg>Automotive</span>
  <span><svg viewBox="0 0 13 11"><polygon points="6.5,1 13,4 6.5,7 0,4"/><rect x="3" y="6" width="7" height="3"/></svg>Education</span>
  <span><svg viewBox="0 0 13 11"><rect x="0" y="3" width="13" height="8" rx="1"/><rect x="4" y="1" width="5" height="2"/></svg>Business and Finance</span>
  <span><svg viewBox="0 0 13 11"><circle cx="6.5" cy="5.5" r="5.5"/></svg>Entertainment</span>
  <span><svg viewBox="0 0 13 11"><rect x="1" y="3" width="3" height="8"/><rect x="5" y="5" width="3" height="6"/><rect x="9" y="3" width="3" height="8"/></svg>Family</span>
  <span><svg viewBox="0 0 13 11"><polygon points="0,1 3,1 4,7 12,7 13,3 3.5,3"/><circle cx="5" cy="9.5" r="1.3"/><circle cx="11" cy="9.5" r="1.3"/></svg>Shopping</span>
</nav>

<section class="intro abs"></section>
<svg class="notch abs" viewBox="0 0 100 34"><polygon points="0,0 100,0 50,34" fill="#ffca27"/></svg>
<div class="more abs">+</div>
<p class="intro-text abs"><span class="lead">Buying a domain can be expensive. There is a lot of money that goes into it and it can be quite a lot for a business to take on,especially if you are a start up company.</span><br>When you go with a local domain lease instead, you will be able to put down less money on the domain. This will give you more money to use for marketing, website building or any other services you need.</p>

<section class="portfolio abs"></section>
<h2 class="section-title portfolio-title abs" style="font-weight:400">
  <svg width="52" height="36" viewBox="0 0 52 36"><rect x="2" y="2" width="38" height="25" rx="2" fill="none" stroke="#351a41" stroke-width="3"/><rect x="15" y="28" width="12" height="4" fill="#351a41"/><rect x="36" y="12" width="14" height="23" rx="2" fill="#351a41" stroke="#ffca27" stroke-width="2"/></svg>
  view our domain portfolio</h2>
<div class="table-card abs"></div>
<div class="tab active abs" style="left:149px;width:173px">ALL DOMAINS</div>
<div class="tab abs" style="left:327px;width:157px">BUY DOMAINS</div>
<div class="tab abs" style="left:489px;width:167px">LEASE DOMAINS</div>
<div class="meta abs"><svg width="14" height="10"><rect y="0" width="14" height="2" fill="#aaa"/><rect y="4" width="14" height="2" fill="#aaa"/><rect y="8" width="14" height="2" fill="#aaa"/></svg>Displaying <b>1 - 75</b> of 63150 Domains</div>
<div class="pager abs"><span class="on">1</span><span>2</span><span>3</span><span>4</span><span>5</span><span>6</span><span>7</span><span>8</span><span>.... Last</span></div>
<div class="sort abs">Fee Decending ▾</div>
<div class="col-head abs" style="left:153px">DOMAIN NAME</div>
<div class="col-head abs" style="left:286px">CATEGORY</div>
<div class="col-head abs" style="left:485px">LEASE FEE</div>
<div class="col-head abs" style="left:614px">PRICE</div>

<div class="row abs" style="top:778px"><span class="name">Credra.example</span><span class="cat"><i></i>Business and Finance</span><span class="fee">$15,500</span><span class="offer">Make Offer</span></div>
<div class="row abs" style="top:800px"><span class="name">Reelix.example</span><span class="cat"><i></i>Automotive</span><span class="fee">$15,500</span><span class="offer">Make Offer</span></div>
<div class="row abs" style="top:822px"><span class="name">Farely.example</span><span class="cat"><i></i>Travel</span><span class="fee">$15,500</span><span class="offer">Make Offer</span></div>
<div class="row abs" style="top:844px"><span class="name">Vitalo.example</span><span class="cat"><i></i>General</span><span class="fee">$15,500</span><span class="offer">Make Offer</span></div>
<div class="row abs" style="top:865px"><span class="name">Motiv.example</span><span class="cat"><i></i>Travel</span><span class="fee">$15,500</span><span class="offer">Make Offer</span></div>

<svg class="scroll abs" viewBox="0 0 12 196"><circle cx="6" cy="7" r="5" fill="none" stroke="#999"/><polygon points="3.5,8.5 8.5,8.5 6,5" fill="#999"/><circle cx="6" cy="188" r="5" fill="none" stroke="#999"/><polygon points="3.5,186.5 8.5,186.5 6,190" fill="#999"/></svg>
<div class="scroll-track abs"></div>
<div class="scroll-thumb abs"></div>

<h2 class="section-title featured-title abs" style="font-weight:400">
  <svg width="50" height="30" viewBox="0 0 50 30"><rect x="1" y="1" width="48" height="28" fill="none" stroke="#351a41" stroke-width="2.5"/><rect x="1" y="1" width="48" height="7" fill="#351a41"/><rect x="8" y="13" width="34" height="2.5" fill="#351a41"/><rect x="8" y="18" width="34" height="2.5" fill="#351a41"/><rect x="8" y="23" width="34" height="2.5" fill="#351a41"/></svg>
  get the featured domains</h2>
<svg class="carousel abs" viewBox="0 0 600 42"><polyline points="17,2 3,21 17,40" fill="none" stroke="#351a41" stroke-width="1.5"/><polyline points="577,2 591,21 577,40" fill="none" stroke="#351a41" stroke-width="1.5"/></svg>
<div class="feature-row abs">
  <div class="feature"><i></i>Credra.example</div>
  <div class="feature"><i></i>Vitalo.example</div>
  <div class="feature"><i></i>Relayo.example</div>
  <div class="feature"><i></i>Carro.example</div>
</div>

<footer class="site-footer abs">
  <div class="foot-col abs" style="left:115px;top:18px"><h3>About Us</h3><ul style="padding-left:3px"><li>News</li><li>Blog</li><li>FAQ</li><li>Success Stories</li></ul></div>
  <div class="foot-col abs" style="left:241px;top:18px"><h3>Lease Domains</h3><ul><li>Premium Domains</li><li>Bargain Domains</li><li>Popular Domains</li><li>Top keywords</li></ul></div>
  <div class="foot-col follow abs" style="left:410px;top:18px"><h3>Follow Us</h3><ul><li><i></i>Friendwall</li><li><i></i>Chirpline</li><li><i></i>Circlesphere</li><li><i></i>Pinboardly</li></ul></div>
  <div class="foot-col abs" style="left:543px;top:18px"><h3>Newsletter</h3></div>
</footer>
<div class="news-input abs">Your E-mail</div>
<div class="btn-subscribe abs">Subscribe</div>
<div class="free-note abs" style="color:#fff">It Is Free !</div>
<div class="btn-signup abs" style="color:#fff">Sign up</div>

</body>
</html>
```